plumweave business card

need to upgrade current business card for an online retailer of handmade arts and crafts, please visit plumweave.com.au

need to be artistic professional look

sample layout, contents, logo, are in the attached files

need for 4 people, details for other 2 people to be provided later

Industry/Entity Type

Business

```html
<!DOCTYPE html>
<html lang="en">
<head>
<meta charset="utf-8">
<title>PlumWeave business card</title>
<link href="https://fonts.googleapis.com/css2?family=Open+Sans:ital,wght@0,400;0,700;1,400&display=swap" rel="stylesheet">
<style>
  :root {
    --stage: #1c1c1c;
    --paper: #ffffff;
    --ink: #3a3330;
    --accent: #d83a2e;
    --rule: #8a8a8a;
    --tagline-tone: #ece9e7;
  }
  html, body {
    margin: 0;
    padding: 0;
    width: 1200px;
    height: 741px;
    overflow: hidden;
    background: var(--stage);
    font-family: "Open Sans", Arial, sans-serif;
    color: var(--ink);
  }
  .canvas { position: relative; width: 1200px; height: 741px; }
  .card {
    position: absolute;
    top: 236px;
    width: 495px;
    height: 282px;
    background: var(--paper);
  }
  .card--front { left: 86px; }
  .card--back { left: 619px; width: 493px; }
  .card__frame {
    position: absolute;
    inset: 18px;
    border: 1px solid var(--rule);
    outline: 1px solid var(--rule);
    outline-offset: -4px;
  }
  .brand-name {
    position: absolute;
    left: 0; right: 0;
    top: 42px;
    text-align: center;
    font-weight: 700;
    font-size: 69px;
    letter-spacing: -1px;
    line-height: 1;
    color: var(--ink);
  }
  .tagline-area {
    position: absolute;
    left: 58px;
    top: 135px;
    width: 387px;
    height: 37px;
    background: var(--tagline-tone);
    border-radius: 3px;
  }
  .holder {
    position: absolute;
    right: 274px;
    top: 203px;
    text-align: right;
  }
  .holder__name {
    font-weight: 700;
    font-size: 21px;
    letter-spacing: 1.3px;
    line-height: 1.1;
  }
  .holder__role {
    font-size: 12.5px;
    color: var(--accent);
    line-height: 1.4;
  }
  .divider {
    position: absolute;
    left: 232px;
    top: 209px;
    width: 2px;
    height: 33px;
    background: var(--ink);
  }
  .contact {
    position: absolute;
    left: 248px;
    top: 208px;
    font-size: 13.8px;
    line-height: 18px;
  }
  .contact__row { display: flex; align-items: center; gap: 8px; }
  .contact__icon { width: 14px; height: 14px; flex: none; }
  .back-copy {
    position: absolute;
    left: 40px; right: 40px;
    margin: 0;
    text-align: center;
    font-size: 14.5px;
  }
  .back-copy--intro { top: 52px; }
  .back-copy--closing { top: 201px; line-height: 19px; }
  .offer-list {
    position: absolute;
    left: 0; right: 0;
    top: 96px;
    margin: 0;
    padding: 0;
    list-style: none;
    text-align: center;
    font-style: italic;
    font-size: 14px;
    line-height: 17.4px;
  }
</style>
</head>
<body>
<main class="canvas">
  <section class="card card--front" aria-label="Card front">
    <div class="card__frame"></div>
    <div class="brand-name">PlumWeave</div>
    <div class="tagline-area" role="img" aria-label="Hand-lettered script tagline"></div>
    <div class="holder">
      <div class="holder__name">Sanjay Thapa</div>
      <div class="holder__role">Director, PlumWeave Australia</div>
    </div>
    <div class="divider"></div>
    <div class="contact">
      <div class="contact__row">
        <svg class="contact__icon" viewBox="0 0 14 14" aria-hidden="true">
          <rect width="14" height="14" fill="#d83a2e"/>
          <path d="M3 5.5c0-1.5 8-1.5 8 0v1H9V5.5H5v1H3z M4 7.5h6l1 3.5H3z" fill="#fff"/>
        </svg>
        <span>+61 400 555 017</span>
      </div>
      <div class="contact__row">
        <svg class="contact__icon" viewBox="0 0 14 14" aria-hidden="true">
          <rect width="14" height="14" fill="#d83a2e"/>
          <rect x="2.5" y="3.5" width="9" height="7" fill="none" stroke="#fff" stroke-width="1"/>
          <path d="M2.5 3.5L7 7.5l4.5-4M2.5 10.5l3.3-3.5M11.5 10.5L8.2 7" fill="none" stroke="#fff" stroke-width="1"/>
        </svg>
        <span>sanjay@plumweave.com.au</span>
      </div>
    </div>
  </section>

  <section class="card card--back" aria-label="Card back">
    <div class="card__frame"></div>
    <p class="back-copy back-copy--intro">Visit us for exotic hand-made arts &amp; crafts around the globe</p>
    <ul class="offer-list">
      <li>-Cashmere Fashion Items From Nepal</li>
      <li>-thai Traditional Painting</li>
      <li>-Nepali/Tibeten Thangkas</li>
      <li>-Lokta/Rice Paper Crafts</li>
      <li>-Allo/Cotton/Woollen Items</li>
    </ul>
    <p class="back-copy back-copy--closing">We encourage eco-Friendly, sustainable and traditional arts practice</p>
  </section>
</main>
</body>
</html>
```